Electrical Services Flyer

We need to create a flyer which will be posted out across Melbourne to businesses to promote our new Electrical Services Division. Services we deliver include but are not limited to - Office Shop fit outs- Lighting and Lighting Automation - Exit and Emergency lighting - Body Corporate works- Thermal Imaging- Test and Tagging- Fault Diagnosis- Switchboard Maintenance/UpgradesFor more on our company please visit kestrinelectrical.com.au

Target Market(s)

Businesses

Colors

Designer to choose colors to be used in the design.

Requirements
Must have
• A modern look, simple clean eye catching.
• A clear way to contact the business
• 152 408
• Quote@kestrin.com.au
Nice to have
• A simple eye catching design that attracts the eye with a simple catchy line like "need an electrician?"

```html
<!DOCTYPE html>
<html lang="en">
<head>
<meta charset="utf-8">
<title>Kestrin Electrical – Electrical Services Flyer</title>
<link rel="stylesheet" href="https://fonts.googleapis.com/css2?family=Raleway:wght@400;500;600&family=Ubuntu:wght@500;700&display=swap">
<style>
  :root {
    --orange: #f0852d;
    --blue: #4155a6;
    --ink: #2f2f33;
    --panel: #353536;
    --paper: #ffffff;
  }
  * { margin: 0; padding: 0; box-sizing: border-box; }
  html, body { width: 956px; height: 1200px; overflow: hidden; background: var(--paper); }
  .flyer { position: relative; width: 956px; height: 1200px; background: var(--paper); font-family: "Raleway", sans-serif; color: var(--ink); overflow: hidden; }

  .brand { position: absolute; left: 59px; top: 45px; display: flex; align-items: center; gap: 12px; }
  .brand-dot { width: 96px; height: 96px; border-radius: 50%; background: var(--orange); }
  .brand-name { font-family: "Ubuntu", sans-serif; font-weight: 700; font-size: 38px; line-height: 1; color: var(--blue); }

  .site-url { position: absolute; left: 593px; top: 89px; font-size: 19.5px; line-height: 24px; letter-spacing: 0.3px; color: var(--ink); white-space: nowrap; }

  .hero-photo { position: absolute; left: 0; top: 174px; width: 956px; height: 449px;
    background: linear-gradient(90deg, #3a3f44 0%, #5b5a55 22%, #6c5f50 40%, #4e5258 62%, #3d4247 100%); }

  .headline { position: absolute; left: 501px; top: 466px; font-family: "Ubuntu", sans-serif; font-weight: 700; color: #fff; font-size: 55px; line-height: 53px; }
  .headline span { display: block; height: 53px; padding: 0 14px 0 13px; width: max-content; white-space: nowrap; }
  .headline .line-blue { background: var(--blue); }
  .headline .line-orange { background: var(--orange); margin-top: 2px; padding-right: 8px; }

  .intro-title { position: absolute; left: 73px; top: 630px; font-size: 38px; font-weight: 500; line-height: 44px; color: var(--ink); white-space: nowrap; }
  .intro-copy { position: absolute; left: 75px; top: 747px; width: 396px; font-size: 16.6px; line-height: 21.9px; text-align: justify; color: var(--ink); }

  .services { position: absolute; left: 117px; top: 920px; list-style: none; }
  .services li { display: flex; align-items: center; gap: 11px; height: 33.8px; font-size: 21px; font-weight: 500; color: var(--ink); white-space: nowrap; }
  .services li::before { content: ""; width: 14px; height: 14px; border-radius: 50%; background: var(--orange); flex: none; }

  .about-panel { position: absolute; left: 508px; top: 633px; width: 448px; height: 334px; background: var(--panel); }
  .about-copy { position: absolute; left: 72px; top: 52px; width: 300px; font-size: 16.6px; line-height: 21.9px; color: #fff; }

  .contact { position: absolute; left: 564px; top: 1024px; }
  .contact-cta { font-family: "Ubuntu", sans-serif; font-weight: 700; font-size: 27px; line-height: 34px; color: var(--orange); white-space: nowrap; }
  .contact-phone { display: flex; align-items: center; gap: 5px; margin-top: 6px; margin-left: 6px; font-size: 28px; line-height: 34px; font-weight: 500; color: var(--ink); }
  .contact-email { display: flex; align-items: center; gap: 9px; margin-top: 0; margin-left: 6px; font-size: 19px; line-height: 24px; letter-spacing: 3.6px; color: var(--ink); white-space: nowrap; }

  .footer-bar { position: absolute; left: 0; bottom: 0; width: 956px; height: 11px; display: flex; }
  .footer-bar .blue { width: 483px; background: var(--blue); }
  .footer-bar .orange { flex: 1; background: var(--orange); }
</style>
</head>
<body>
<main class="flyer">
  <header>
    <div class="brand">
      <div class="brand-dot"></div>
      <div class="brand-name">Kestrin Electrical</div>
    </div>
    <div class="site-url">www.kestrinelectrical.com.au</div>
  </header>

  <div class="hero-photo" role="img" aria-label="Electrician in a hard hat and red shirt carrying a yellow ladder through a steel-framed building site"></div>

  <h1 class="headline">
    <span class="line-blue">NEED AN</span>
    <span class="line-orange">ELECTRICIAN?</span>
  </h1>

  <h2 class="intro-title">Qualified and ready<br>to work on any project.</h2>
  <p class="intro-copy">Our innovative division is led by qualified / licensed electricians and experienced estimators with over 20 years’ experience over a wide variety of industrial and commercial electrical contracting works. We're trusted by a wide client base across Melbourne - including commercial and industrial builders.</p>

  <ul class="services">
    <li>General electrical</li>
    <li>MATV</li>
    <li>Fire detection/warning systems</li>
    <li>Access control</li>
    <li>Nurse call</li>
    <li>Certified communications</li>
    <li>Data and optical fibre systems</li>
  </ul>

  <section class="about-panel">
    <p class="about-copy">At Kestrin Electrical have rapidly gained a reputation as a company that gets the job done right. From estimating, technical advice to project completion. Our track record across a wide variety of electrical work, means we can handle just about any job, and ensure every project is completed to the highest industry standard.</p>
  </section>

  <section class="contact">
    <p class="contact-cta">Get a free quote today!</p>
    <p class="contact-phone">
      <svg width="20" height="22" viewBox="0 0 18 20" aria-hidden="true"><path d="M4 1 L7 5 L5.5 7.5 C6.5 10 8 12 10.5 13.5 L13 12 L17 15 L15 18.5 C9 19 2 12 1.5 4 Z" fill="none" stroke="#f0852d" stroke-width="1.8" stroke-linejoin="round"/></svg>
      152 408
    </p>
    <p class="contact-email">
      <svg width="14" height="10" viewBox="0 0 14 10" aria-hidden="true"><rect x="0" y="0" width="14" height="10" fill="#f0852d"/><path d="M0 0 L7 6 L14 0" fill="none" stroke="#fff" stroke-width="1.3"/></svg>
      Quote@kestrin.com.au
    </p>
  </section>

  <div class="footer-bar"><div class="blue"></div><div class="orange"></div></div>
</main>
</body>
</html>
```